Awesome photographers card for an awesome new business

Double sided business card Black background and silver logo in middle on one side. Details on otherside. please keep it simple

Photographer

Gavin Tolley
0482615073
GavinTolleyPhotography82@lumenpost.com
www.GavinTolleyPhotography.com.au
Instagram _Gavin_tolley

Requirements
Must have
• My logo in Silver
• please use instagram logo instead of "Instagram"

```html
<!DOCTYPE html>
<html lang="en">
<head>
<meta charset="utf-8">
<title>Gavin Tolley Photography – Business Card</title>
<link rel="stylesheet" href="https://fonts.googleapis.com/css2?family=Montserrat:wght@300;400;700&display=swap">
<style>
  :root {
    --page: #1c1c1c;
    --card-dark: #050505;
    --card-light: #2a2a2a;
    --silver: #d9d9d9;
    --silver-soft: #a8a8a8;
    --white: #f4f4f4;
  }
  * { box-sizing: border-box; margin: 0; padding: 0; }
  html, body { width: 1200px; height: 791px; overflow: hidden; }
  body {
    background: var(--page);
    font-family: "Montserrat", sans-serif;
    display: flex;
    flex-direction: column;
    align-items: center;
    justify-content: center;
    gap: 40px;
  }
  .card {
    position: relative;
    width: 600px;
    height: 330px;
    background: var(--card-dark);
    overflow: hidden;
    box-shadow: 0 10px 30px rgba(0,0,0,.5);
  }
  .card__sheen {
    position: absolute;
    inset: 0;
    background: linear-gradient(135deg, #3a3a3a, var(--card-light) 50%, #151515);
    clip-path: polygon(62% 0, 100% 0, 100% 100%, 30% 100%);
  }
  .card__edge {
    position: absolute;
    left: 0; right: 0; bottom: 10px;
    height: 7px;
    border-top: 1.5px solid var(--white);
    border-bottom: 1.5px solid var(--white);
  }
  .brand {
    position: absolute;
    display: flex;
    align-items: center;
    gap: 14px;
    color: var(--silver);
    font-weight: 400;
    font-size: 17px;
    letter-spacing: .08em;
    text-transform: uppercase;
    line-height: 1.3;
  }
  .brand__ring {
    width: 64px; height: 64px;
    border: 3px solid var(--silver);
    border-radius: 50%;
    flex: none;
  }
  .card--front .brand { left: 170px; top: 110px; }
  .card--front .website {
    position: absolute;
    left: 170px; bottom: 48px;
    color: var(--silver);
    font-size: 15px;
    font-weight: 300;
    letter-spacing: .12em;
  }
  .card--back .brand { left: 36px; top: 120px; font-size: 14px; }
  .contact {
    position: absolute;
    right: 32px; top: 70px;
    text-align: right;
    color: var(--white);
  }
  .contact__name {
    font-size: 26px;
    font-weight: 300;
    margin-bottom: 14px;
  }
  .contact__name b { font-weight: 700; }
  .contact__list { list-style: none; font-size: 13px; font-weight: 300; }
  .contact__list li {
    display: flex;
    justify-content: flex-end;
    align-items: center;
    gap: 8px;
    height: 24px;
  }
  .contact__icon { width: 14px; height: 14px; flex: none; }
</style>
</head>
<body>

  <section class="card card--front">
    <div class="card__sheen"></div>
    <div class="brand">
      <span class="brand__ring"></span>
      <span>Gavin Tolley<br>Photography</span>
    </div>
    <p class="website">www.GavinTolleyPhotography.com.au</p>
    <div class="card__edge"></div>
  </section>

  <section class="card card--back">
    <div class="card__sheen"></div>
    <div class="brand">
      <span class="brand__ring"></span>
      <span>Gavin Tolley<br>Photography</span>
    </div>
    <div class="contact">
      <h1 class="contact__name">Gavin <b>Tolley</b></h1>
      <ul class="contact__list">
        <li>0482615073
          <svg class="contact__icon" viewBox="0 0 16 16"><circle cx="8" cy="8" r="7.2" fill="none" stroke="#f4f4f4" stroke-width="1.2"/><path d="M5.5 4.5l1.3 1.6-.8 1c.6 1.2 1.4 2 2.6 2.6l1-.8 1.6 1.3-.9 1.3C7.8 11.3 4.9 8.4 4.2 5.4z" fill="#f4f4f4"/></svg>
        </li>
        <li>GavinTolleyPhotography82@lumenpost.com
          <svg class="contact__icon" viewBox="0 0 16 16"><rect x="1" y="3.5" width="14" height="9" fill="#f4f4f4"/><path d="M1 3.5l7 5 7-5" fill="none" stroke="#050505" stroke-width="1.2"/></svg>
        </li>
        <li>www.GavinTolleyPhotography.com.au
          <svg class="contact__icon" viewBox="0 0 16 16" fill="none" stroke="#f4f4f4" stroke-width="1.1"><circle cx="8" cy="8" r="6.8"/><ellipse cx="8" cy="8" rx="3" ry="6.8"/><path d="M1.2 8h13.6M2.5 4.5h11M2.5 11.5h11"/></svg>
        </li>
        <li>_Gavin_tolley
          <svg class="contact__icon" viewBox="0 0 16 16"><rect x="1" y="1" width="14" height="14" rx="2" fill="#f4f4f4"/></svg>
        </li>
      </ul>
    </div>
    <div class="card__edge"></div>
  </section>

</body>
</html>
```